TL Estates
Desmond Parkes
TL Estates - Real Estate
Creative Brief
Corporate
Owner/ Realtor
Suite # 17 Ashbury Business Centre, 28 Calder Rd. Kingston 5
dp@desmondparkes-example.com
www.desmondparkes-example.com
Business card , Letter head and envelopes to compliment LOGO i DO NOT WANT MY PICTURE TO APPEAR IN A BOX...I WOULD WANT IT TO BE FLOATING ON THE BUSINESS CARD I would like for the designers to colour my shirt RED

```html
<!DOCTYPE html>
<html lang="en">
<head>
<meta charset="utf-8">
<title>TL Estates – Business Card</title>
<link href="https://fonts.googleapis.com/css2?family=Cinzel:wght@600;700&family=Tinos:wght@400;700&family=Arimo:wght@700&display=swap" rel="stylesheet">
<style>
  :root {
    --backdrop: #2f2f2f;
    --card: #ffffff;
    --red: #c4161c;
    --red-dark: #7d0a0e;
    --ink: #1a1a1a;
    --text: #333333;
    --badge-blue: #3a78c2;
    --skin: #6b4632;
  }
  * { margin: 0; padding: 0; box-sizing: border-box; }
  html, body {
    width: 1200px; height: 780px; overflow: hidden;
    background: var(--backdrop);
  }
  .canvas { position: relative; width: 1200px; height: 780px; }
  .card {
    position: absolute; left: 100px; top: 105px;
    width: 1000px; height: 570px;
    background: var(--card);
    border-radius: 26px;
    overflow: hidden;
    box-shadow: 0 12px 30px rgba(0,0,0,.45);
  }
  .card-swooshes { position: absolute; inset: 0; width: 100%; height: 100%; }

  .portrait {
    position: absolute; left: 70px; top: 70px;
    width: 280px; height: 290px;
    border-radius: 48% 48% 22% 22% / 40% 40% 18% 18%;
    background:
      radial-gradient(ellipse 28% 30% at 50% 30%, var(--skin) 0 70%, transparent 100%),
      linear-gradient(180deg, transparent 0 48%, #e8502f 58%, #d8391f 100%);
    filter: blur(1px);
  }

  .agent {
    position: absolute; left: 40px; top: 385px; width: 300px;
    text-align: center;
  }
  .agent-name {
    font-family: "Arimo", sans-serif; font-weight: 700;
    font-size: 27px; color: var(--red);
  }
  .agent-title {
    font-family: "Arimo", sans-serif; font-weight: 700;
    font-size: 20px; color: var(--ink); margin-top: 4px;
  }
  .badges { display: flex; justify-content: center; gap: 10px; margin-top: 14px; }
  .badge { display: block; border-radius: 3px; }
  .badge-listing { width: 58px; height: 30px; background: var(--badge-blue); }
  .badge-member { width: 28px; height: 30px; background: var(--badge-blue); opacity: .8; }

  .brand {
    position: absolute; left: 470px; top: 45px; width: 330px;
    display: flex; align-items: center; justify-content: center; gap: 14px;
  }
  .brand-square {
    width: 88px; height: 88px; background: var(--red);
    box-shadow: 0 3px 6px rgba(0,0,0,.3);
  }
  .brand-name {
    font-family: "Cinzel", serif; font-weight: 700;
    font-size: 28px; color: var(--red);
  }

  .headline {
    position: absolute; left: 380px; top: 160px; width: 540px;
    text-align: center;
  }
  .headline-name {
    font-family: "Cinzel", serif; font-weight: 700;
    font-size: 44px; letter-spacing: 1px; color: var(--red);
    line-height: 1; white-space: nowrap;
  }
  .headline-tagline {
    font-family: "Tinos", serif; font-weight: 700;
    font-size: 14px; letter-spacing: 2px; color: var(--ink); margin-top: 6px;
    white-space: nowrap;
  }

  .address {
    position: absolute; right: 100px; top: 248px;
    text-align: right; font-style: normal;
    font-family: "Tinos", serif; font-size: 22px; line-height: 1.3; color: var(--text);
    white-space: nowrap;
  }

  .contacts {
    position: absolute; right: 100px; top: 330px;
    font-family: "Tinos", serif; font-size: 21px; color: var(--text);
  }
  .contact-row {
    display: flex; justify-content: flex-end; gap: 22px; margin-bottom: 16px;
    white-space: nowrap;
  }
  .contact { display: flex; align-items: center; gap: 8px; }
  .contact svg { width: 21px; height: 21px; fill: var(--red); }
  .website { text-align: right; font-size: 22px; white-space: nowrap; }
</style>
</head>
<body>
<main class="canvas">
  <section class="card" aria-label="TL Estates business card">
    <svg class="card-swooshes" viewBox="0 0 1000 570" preserveAspectRatio="none" aria-hidden="true">
      <defs>
        <linearGradient id="redSweep" x1="0" y1="0" x2="1" y2="1">
          <stop offset="0" stop-color="#d8242a"/>
          <stop offset="1" stop-color="#7d0a0e"/>
        </linearGradient>
      </defs>
      <path d="M640,0 C820,18 945,95 1000,225 L1000,195 C950,92 850,28 700,0 Z" fill="#111"/>
      <path d="M700,0 L1000,0 L1000,195 C950,92 850,28 700,0 Z" fill="url(#redSweep)"/>
      <path d="M0,320 C70,455 190,530 400,570 L350,570 C170,540 60,470 0,360 Z" fill="#111"/>
      <path d="M0,360 C60,470 170,540 350,570 L0,570 Z" fill="url(#redSweep)"/>
    </svg>

    <div class="portrait" role="img" aria-label="Portrait of Desmond Parkes in a red shirt, floating without a frame"></div>

    <div class="agent">
      <p class="agent-name">Desmond Parkes</p>
      <p class="agent-title">CEO/Realtor</p>
      <div class="badges">
        <span class="badge badge-listing"></span>
        <span class="badge badge-member"></span>
      </div>
    </div>

    <div class="brand">
      <span class="brand-square"></span>
      <span class="brand-name">TL Estates</span>
    </div>

    <div class="headline">
      <h1 class="headline-name">DESMOND PARKES</h1>
      <p class="headline-tagline">REAL ESTATE, REAL PEOPLE</p>
    </div>

    <address class="address">
      Suite 17, Ashbury Business Centre<br>
      28 Calder Road, Kingston 5.
    </address>

    <div class="contacts">
      <div class="contact-row">
        <span class="contact">
          <svg viewBox="0 0 24 24"><path d="M6.6 10.8a15 15 0 0 0 6.6 6.6l2.2-2.2c.3-.3.7-.4 1-.2 1.1.4 2.3.6 3.6.6.6 0 1 .4 1 1V20c0 .6-.4 1-1 1A17 17 0 0 1 3 4c0-.6.4-1 1-1h3.5c.6 0 1 .4 1 1 0 1.3.2 2.5.6 3.6.1.3 0 .7-.2 1z"/></svg>
          876-5550142
        </span>
        <span class="contact">
          <svg viewBox="0 0 24 24"><path d="M7 1h10a2 2 0 0 1 2 2v18a2 2 0 0 1-2 2H7a2 2 0 0 1-2-2V3a2 2 0 0 1 2-2zm0 4v13h10V5zm5 14.5a1.2 1.2 0 1 0 0 2.4 1.2 1.2 0 0 0 0-2.4z"/></svg>
          876-5550187
        </span>
      </div>
      <div class="contact-row">
        <span class="contact">
          <svg viewBox="0 0 24 24"><path d="M6 2h12v6H6zM4 9h16a2 2 0 0 1 2 2v7h-4v4H6v-4H2v-7a2 2 0 0 1 2-2zm4 7v4h8v-4z"/></svg>
          876-5550163
        </span>
        <span class="contact">
          <svg viewBox="0 0 24 24"><path d="M12 2a10 10 0 1 0 5 18.7l-1-1.7A8 8 0 1 1 20 12v1a2 2 0 0 1-4 0V7h-2v1a5 5 0 1 0 .8 6.8A4 4 0 0 0 22 13v-1A10 10 0 0 0 12 2zm0 13a3 3 0 1 1 0-6 3 3 0 0 1 0 6z"/></svg>
          dp@desmondparkes-example.com
        </span>
      </div>
      <p class="website">www.desmondparkes-example.com</p>
    </div>
  </section>
</main>
</body>
</html>
```